3 out of 100 people will get deadly skin cancer - we need a great illustration that shows this!

We put together a prototype image that communicates lifetime skin cancer risk. (see attached). We are looking for illustrators who can take make a new/better/cooler graphic that communicates this idea. It could be as simple as a superior illustration of the graphic we have or illustrators can propose a completely different idea.What should the illustration communicate?U.S. adults have a lifetime risk of developing skin cancer of 1 in 5. But we don't want to show 1 in 5; we want to show that number in a larger group. For example, in the attached illustration we show 20 in 100 people get skin cancer (i.e., 100 beach towels/umbrellas and 20 of them are red). Research has shown that people are more likely to accurately understand numbers like this when you convey them for larger groups (i.e., 20 out of 100 rather than 1 out of 5). U.S. adults also have a lifetime risk of 2.3% of developing the deadliest form of skin cancer (melanoma). In other words, approximately 3 in 100 people will develop melanoma in their lifetime. Ideally, a single image will convey both lifetime skin cancer risk (20 in 100) and melanoma risk (3 in 100). We will award a top three as follows: 1st place = $300, 2nd place = $250, third place = $200. We will also buy any design beyond 3rd place that we like for $100. For example, we purchased 24 designs in our last contest on Artquilla.This research is supported by funding from the University of Brenmoor.

Target Market(s)

The U.S. public; individuals at high risk of developing skin cancer

Industry/Entity Type

Medicine

Colors

Designer to choose colors to be used in the design.

Requirements
Must have
• an original illustration that conveys both lifetime risk of developing skin cancer (20 in 100) and melanoma (3 in 100).
Nice to have
• It can be beach towels and umbrellas, just like our prototype, or the designers can pitch an original idea. Imagery can be realistic or cartoonish (or something in between). It should be illustrations, though. Not edited photos. The image should be in color (no black and white illustrations).
Should not have
• Photos. Clip art. Free vector images.
• We are looking for original illustrations created by the designer.

```html
<!DOCTYPE html>
<html lang="en">
<head>
<meta charset="utf-8">
<title>How likely are you to get skin cancer?</title>
<link rel="stylesheet" href="https://fonts.googleapis.com/css2?family=Anton&family=Arimo&family=Fira+Sans:wght@400&display=swap">
<style>
  :root {
    --sand-top: #ffa85a;
    --sand-mid: #ffc48a;
    --sand-low: #fdd7ab;
    --title: #4d5c8c;
    --subtitle: #5a69a3;
    --sea-top: #4fd8f2;
    --sea-bottom: #3fc6e4;
    --foam: #eafaff;
    --heading: #2d5a91;
    --body: #ffffff;
    --towel-clear: #cfe6f3;
    --towel-cancer: #f2a488;
    --towel-melanoma: #d9573d;
    --sun: #f59a2c;
  }
  * { margin: 0; padding: 0; box-sizing: border-box; }
  html, body { width: 1200px; height: 4571px; overflow: hidden; }
  body {
    position: relative;
    background: linear-gradient(180deg, var(--sand-top) 0px, var(--sand-mid) 1200px, var(--sand-low) 3100px);
    font-family: "Arimo", Arial, sans-serif;
  }
  .title {
    position: absolute; left: 56px; top: 58px;
    font-family: "Anton", Impact, sans-serif;
    font-size: 70px; line-height: 1; color: var(--title);
    letter-spacing: -0.5px;
  }
  .intro {
    position: absolute; left: 57px; top: 164px;
    font-size: 38px; line-height: 59px; color: var(--subtitle);
  }
  .sun-art {
    position: absolute; left: 80px; top: 390px; width: 375px; height: 470px;
    background: radial-gradient(circle at 45% 35%, var(--sun) 0 42%, rgba(245,154,44,0.35) 60%, transparent 72%);
  }
  .legend { position: absolute; left: 565px; top: 444px; }
  .legend-row { display: flex; align-items: center; height: 124px; margin-bottom: 17px; }
  .legend-row svg { width: 145px; height: 124px; }
  .legend-label {
    margin-left: 24px; font-size: 52px; color: var(--subtitle);
    font-family: "Arimo", Arial, sans-serif;
  }
  .towel-grid { position: absolute; left: 70px; top: 1025px; }
  .sea { position: absolute; left: 0; top: 3120px; width: 1200px; height: 1451px; }
  .advice { position: absolute; left: 78px; width: 1060px; font-family: "Fira Sans", sans-serif; }
  .advice h2 { font-weight: 400; font-size: 40px; line-height: 48px; color: var(--heading); }
  .advice p { font-size: 36px; line-height: 35px; color: var(--body); text-align: justify; margin-left: 4px; }
</style>
</head>
<body>
  <h1 class="title">How likely are you to get skin cancer?</h1>
  <p class="intro">Let's say 100 people go to the beach<br>How many will develop skin cancer in their lifetime?<br>How many melanoma, the deadliest form of skin cancer?</p>

  <div class="sun-art" role="img" aria-label="Illustration of a cartoon sun drawing a bow and arrow"></div>

  <div class="legend">
    <div class="legend-row">
      <svg viewBox="0 0 145 124"><rect x="0" y="0" width="62" height="124" rx="3" fill="var(--towel-clear)"/><rect x="82" y="0" width="62" height="124" rx="3" fill="var(--towel-clear)"/></svg>
      <span class="legend-label">= no skin cancer</span>
    </div>
    <div class="legend-row">
      <svg viewBox="0 0 145 124"><rect x="0" y="0" width="62" height="124" rx="3" fill="var(--towel-cancer)"/><rect x="82" y="0" width="62" height="124" rx="3" fill="var(--towel-cancer)"/></svg>
      <span class="legend-label">= skin cancer</span>
    </div>
    <div class="legend-row">
      <svg viewBox="0 0 145 124"><rect x="0" y="0" width="62" height="124" rx="3" fill="var(--towel-melanoma)"/><rect x="82" y="0" width="62" height="124" rx="3" fill="var(--towel-melanoma)"/></svg>
      <span class="legend-label">= melanoma</span>
    </div>
  </div>

  <svg class="towel-grid" width="1060" height="1900" viewBox="0 0 1060 1900" role="img" aria-label="100 beach towels: 80 without skin cancer, 17 with skin cancer, 3 with melanoma">
    <defs>
      <rect id="towel" width="80" height="162" rx="3"/>
    </defs>
    <g fill="var(--towel-clear)">
      <!-- row 1 -->
      <use href="#towel" x="0" y="0"/><use href="#towel" x="105" y="0"/><use href="#towel" x="210" y="0"/><use href="#towel" x="315" y="0"/><use href="#towel" x="525" y="0"/><use href="#towel" x="630" y="0"/><use href="#towel" x="840" y="0"/><use href="#towel" x="945" y="0"/>
      <!-- row 2 -->
      <use href="#towel" x="0" y="190"/><use href="#towel" x="105" y="190"/><use href="#towel" x="315" y="190"/><use href="#towel" x="420" y="190"/><use href="#towel" x="525" y="190"/><use href="#towel" x="735" y="190"/><use href="#towel" x="840" y="190"/>
      <!-- row 3 -->
      <use href="#towel" x="0" y="380"/><use href="#towel" x="210" y="380"/><use href="#towel" x="315" y="380"/><use href="#towel" x="525" y="380"/><use href="#towel" x="735" y="380"/><use href="#towel" x="840" y="380"/><use href="#towel" x="945" y="380"/>
      <!-- row 4 -->
      <use href="#towel" x="0" y="570"/><use href="#towel" x="105" y="570"/><use href="#towel" x="210" y="570"/><use href="#towel" x="315" y="570"/><use href="#towel" x="420" y="570"/><use href="#towel" x="630" y="570"/><use href="#towel" x="735" y="570"/><use href="#towel" x="840" y="570"/><use href="#towel" x="945" y="570"/>
      <!-- row 5 -->
      <use href="#towel" x="0" y="760"/><use href="#towel" x="105" y="760"/><use href="#towel" x="315" y="760"/><use href="#towel" x="420" y="760"/><use href="#towel" x="525" y="760"/><use href="#towel" x="630" y="760"/><use href="#towel" x="840" y="760"/><use href="#towel" x="945" y="760"/>
      <!-- row 6 -->
      <use href="#towel" x="0" y="950"/><use href="#towel" x="105" y="950"/><use href="#towel" x="210" y="950"/><use href="#towel" x="315" y="950"/><use href="#towel" x="525" y="950"/><use href="#towel" x="630" y="950"/><use href="#towel" x="840" y="950"/><use href="#towel" x="945" y="950"/>
      <!-- row 7 -->
      <use href="#towel" x="105" y="1140"/><use href="#towel" x="210" y="1140"/><use href="#towel" x="315" y="1140"/><use href="#towel" x="420" y="1140"/><use href="#towel" x="525" y="1140"/><use href="#towel" x="630" y="1140"/><use href="#towel" x="735" y="1140"/><use href="#towel" x="840" y="1140"/>
      <!-- row 8 -->
      <use href="#towel" x="0" y="1330"/><use href="#towel" x="105" y="1330"/><use href="#towel" x="210" y="1330"/><use href="#towel" x="315" y="1330"/><use href="#towel" x="630" y="1330"/><use href="#towel" x="735" y="1330"/><use href="#towel" x="840" y="1330"/><use href="#towel" x="945" y="1330"/>
      <!-- row 9 -->
      <use href="#towel" x="0" y="1520"/><use href="#towel" x="105" y="1520"/><use href="#towel" x="210" y="1520"/><use href="#towel" x="315" y="1520"/><use href="#towel" x="420" y="1520"/><use href="#towel" x="525" y="1520"/><use href="#towel" x="630" y="1520"/><use href="#towel" x="840" y="1520"/><use href="#towel" x="945" y="1520"/>
      <!-- row 10 -->
      <use href="#towel" x="0" y="1710"/><use href="#towel" x="105" y="1710"/><use href="#towel" x="315" y="1710"/><use href="#towel" x="420" y="1710"/><use href="#towel" x="525" y="1710"/><use href="#towel" x="630" y="1710"/><use href="#towel" x="735" y="1710"/><use href="#towel" x="840" y="1710"/>
    </g>
    <g fill="var(--towel-cancer)">
      <use href="#towel" x="420" y="0"/><use href="#towel" x="735" y="0"/>
      <use href="#towel" x="210" y="190"/><use href="#towel" x="945" y="190"/>
      <use href="#towel" x="105" y="380"/><use href="#towel" x="420" y="380"/><use href="#towel" x="630" y="380"/>
      <use href="#towel" x="210" y="760"/><use href="#towel" x="735" y="760"/>
      <use href="#towel" x="735" y="950"/>
      <use href="#towel" x="0" y="1140"/><use href="#towel" x="945" y="1140"/>
      <use href="#towel" x="420" y="1330"/><use href="#towel" x="525" y="1330"/>
      <use href="#towel" x="735" y="1520"/>
      <use href="#towel" x="210" y="1710"/><use href="#towel" x="945" y="1710"/>
    </g>
    <g fill="var(--towel-melanoma)">
      <use href="#towel" x="630" y="190"/>
      <use href="#towel" x="525" y="570"/>
      <use href="#towel" x="420" y="950"/>
    </g>
  </svg>

  <svg class="sea" viewBox="0 0 1200 1451" preserveAspectRatio="none" aria-hidden="true">
    <defs>
      <linearGradient id="seaFill" x1="0" y1="0" x2="0" y2="1">
        <stop offset="0" stop-color="var(--sea-top)"/>
        <stop offset="1" stop-color="var(--sea-bottom)"/>
      </linearGradient>
    </defs>
    <path d="M0 60 C80 20 150 70 230 40 S380 10 460 45 S620 70 700 35 S860 15 940 50 S1100 70 1200 30 L1200 1451 L0 1451 Z" fill="var(--foam)"/>
    <path d="M0 90 C90 55 170 100 250 75 S400 50 480 85 S640 105 720 70 S880 55 960 90 S1110 100 1200 65 L1200 1451 L0 1451 Z" fill="url(#seaFill)"/>
  </svg>

  <section class="advice" style="top:3385px">
    <h2>What can you do to prevent skin cancer?</h2>
    <p>Leading medical experts, including those at Halvern Clinic, make these recommendations for preventing skin cancer</p>
  </section>
  <section class="advice" style="top:3563px">
    <h2>Avoid the sun from 10 a.m. to 4 p.m.</h2>
    <p>These are the peak hours sunstrength in North America - even in the winter and on cloudy days.</p>
  </section>
  <section class="advice" style="top:3738px">
    <h2>Wear sunscreen</h2>
    <p>Reapply sunscreen every two hours or more frequently if you're swimming or sweating</p>
  </section>
  <section class="advice" style="top:3912px">
    <h2>Wear protective clothing</h2>
    <p>Hats with wide brims and clothing that covers your arms and legs are helpful. Sunscreen doesn't block all UV rays, which cause skin cancer</p>
  </section>
  <section class="advice" style="top:4122px">
    <h2>Avoid tanning beds</h2>
    <p>Tanning beds operate with UV lights, damaging your skin and potentially leading to cancer.</p>
  </section>
  <section class="advice" style="top:4298px">
    <h2>Self-check your skin</h2>
    <p style="color:var(--heading)">If you notice differences, talk with your health care team</p>
  </section>
</body>
</html>
```